Need A Standard Musical Download Website

We are looking for a talented designer to create a unique web design for our startup Music website called Vorlen Music.
The website should be responsive and filled with some creative stuffs along with bright colors.

Vorlen music is a website loaded with different types of music and capable of downloading the requested music by its users.
There will be categories of music which would be sorted by the genre. They include RnB, Hip-Hop, Afro pop, Pop, Dancehall and Reggae).

DESIGN STYLE/THEME

Creative, trendy, colorful, unique, and easy to use. You have freedom of selecting which ever color suits you. The design must be energetic and attractive.

NAVIGATION

HOME-MUSIC(RnB, Hip hop, Afro pop, POP, dancehall, Reggae)-ARTISTE-NEWS-LOGIN

PAGES REQUIRED
------------
1)Home Page
2)Music

FONTS
GOOGLE FONTS is strongly recommended.

Designers can get inspiration from https://tunebarrowk.com

Industry/Entity Type

Startup

```html
<!DOCTYPE html>
<html lang="en">
<head>
<meta charset="utf-8">
<title>Vorlen Music</title>
<link rel="stylesheet" href="https://fonts.googleapis.com/css2?family=Roboto:wght@400;500;700&family=Lora:ital@1&display=swap">
<style>
:root{
  --page:#f6f7f9;
  --red:#f0281e;
  --red-dark:#d81c12;
  --nav:#3f3f3f;
  --ink:#4a4a4a;
  --muted:#7c7c7c;
  --green-top:#6cc04a;
  --green-bottom:#3a9b23;
  --line:#d4d4d4;
}
*{box-sizing:border-box;margin:0;padding:0}
html,body{width:1200px;height:1065px;overflow:hidden;background:var(--page);font-family:Roboto,Arial,sans-serif}
.page{position:relative;width:1200px;height:1065px}
.brand{position:absolute;top:20px;left:0;width:1200px;display:flex;justify-content:center;align-items:center;gap:14px}
.brand-mark{width:60px;height:60px;border-radius:50%;background:var(--red)}
.brand-name{font-size:32px;font-weight:500;color:var(--ink);letter-spacing:.5px}
.main-nav{position:absolute;top:111px;left:86px;width:1028px;height:57px;display:flex;background:var(--nav)}
.main-nav a{display:flex;align-items:center;justify-content:center;color:#fff;text-decoration:none;font-size:16px;font-weight:500;border-right:1px solid #fff}
.main-nav a:last-child{border-right:0}
.main-nav a.active{background:var(--red)}
.hero{position:absolute;top:169px;left:86px;width:686px;height:474px;background:radial-gradient(ellipse at 50% 25%,#7a3fb5 0%,#3e2366 35%,#1d1627 70%,#120f16 100%);text-align:center;color:#fff}
.hero h1{position:absolute;top:148px;width:100%;font-size:51px;font-weight:700;letter-spacing:.5px}
.hero p{position:absolute;top:212px;left:60px;width:566px;font-family:Lora,Georgia,serif;font-style:italic;font-size:14.5px;line-height:31.5px}
.hero-btn{position:absolute;top:323px;left:197px;width:294px;height:46px;border-radius:3px;background:linear-gradient(#f53a2c,var(--red-dark));display:flex;align-items:center;justify-content:center;font-size:16px;font-weight:500;letter-spacing:.3px}
.quote{position:absolute;top:169px;left:773px;width:341px;height:474px;background:var(--red);color:#fff}
.quote h2{position:absolute;top:38px;width:100%;text-align:center;font-size:21px;font-weight:700}
.field{position:absolute;left:22px;width:299px;height:42px;background:#fff;border-radius:2px;color:#777;font-size:13px;font-family:Arial,sans-serif;display:flex;align-items:center;padding-left:14px}
.field .caret{position:absolute;right:22px;top:18px;border:5px solid transparent;border-top-color:#555}
.opt-in{position:absolute;top:306px;left:24px;display:flex;align-items:center;gap:12px;font-size:14px;font-family:Arial,sans-serif}
.opt-in span.box{width:12px;height:12px;background:#fff;border-radius:3px}
.quote-btn{position:absolute;top:350px;left:24px;width:294px;height:47px;border-radius:3px;background:linear-gradient(var(--green-top),var(--green-bottom));display:flex;align-items:center;justify-content:center;font-size:19px;font-weight:500}
.quote-links{position:absolute;top:410px;left:24px;width:294px;display:flex;justify-content:space-between;font-size:13px;font-family:Arial,sans-serif}
.quote-links .secure{display:flex;align-items:center;gap:5px}
.genres{position:absolute;top:644px;left:86px;width:1028px;height:189px;background:linear-gradient(#d7d7d7,#f0f0f0 75%,#fafafa);display:flex;box-shadow:0 2px 3px rgba(0,0,0,.08)}
.genre{position:relative;flex:1}
.genre+.genre{box-shadow:inset 8px 0 8px -6px rgba(0,0,0,.18)}
.genre-art{position:absolute;top:28px;left:13px;width:82px;height:112px;background:#c4c4c4;border-radius:4px}
.genre h3{position:absolute;top:28px;left:128px;font-size:16px;font-weight:500;color:#3c3c3c}
.genre p{position:absolute;top:59px;left:128px;width:200px;font-size:12px;line-height:21.4px;color:var(--muted);font-family:Arial,sans-serif}
.social{position:absolute;top:878px;left:390px;display:flex;gap:10px}
.social span{width:60px;height:60px;border:1px solid #ccc;border-radius:50%;display:flex;align-items:center;justify-content:center}
.footer-nav{position:absolute;top:969px;left:0;width:1200px;display:flex;justify-content:center;gap:38px;font-size:13px;color:#6e6e6e;font-family:Arial,sans-serif}
.copy{position:absolute;top:1015px;left:0;width:1200px;text-align:center;font-size:12px;color:#777;font-family:Arial,sans-serif}
</style>
</head>
<body>
<div class="page">
  <header class="brand">
    <span class="brand-mark"></span>
    <span class="brand-name">VORLEN MUSIC</span>
  </header>

  <nav class="main-nav">
    <a class="active" style="width:211px">HOME</a>
    <a style="width:200px">MUSIC</a>
    <a style="width:210px">ARTISTE</a>
    <a style="width:196px">NEWS</a>
    <a style="width:211px">LOGIN</a>
  </nav>

  <section class="hero" role="img" aria-label="Concert crowd in front of a purple-lit stage">
    <h1>VORLEN MUSIC</h1>
    <p>Sed ut perspiciatis unde omnis iste natus error sit voluptatem accusantium doloremque laudantium, totam rem aperiam, eaque ipsa quae ab illo inventore veritatis et quasi archi-tecto beatae vitae dicta sunt explicabo.</p>
    <div class="hero-btn">DOWNLOAD UP TO 15 SONGS</div>
  </section>

  <aside class="quote">
    <h2>REQUEST QUOTE</h2>
    <div class="field" style="top:88px">Email Address :</div>
    <div class="field" style="top:140px">Password :</div>
    <div class="field" style="top:192px">Re - Enter Password :</div>
    <div class="field" style="top:244px">Country :<span class="caret"></span></div>
    <div class="opt-in"><span class="box"></span>Email me about new &amp; Free Music</div>
    <div class="quote-btn">REQUEST QUOTE</div>
    <div class="quote-links">
      <span>Terms and Conditions</span>
      <span class="secure"><svg width="10" height="12" viewBox="0 0 10 12"><path d="M2 5V3.5a3 3 0 0 1 6 0V5" fill="none" stroke="#fff" stroke-width="1.6"/><rect x="0.5" y="5" width="9" height="7" rx="1" fill="#fff"/></svg>Secure Server</span>
    </div>
  </aside>

  <section class="genres">
    <div class="genre">
      <div class="genre-art" role="img" aria-label="Illustration of a rapper with a microphone"></div>
      <h3>HIP-HOP</h3>
      <p>Sed ut perspiciatis unde omnis iste natus error sit voluptatem accusan-tium doloremque laudantium, totam dicta sunt explicabo.</p>
    </div>
    <div class="genre">
      <svg class="note" style="position:absolute;top:38px;left:18px" width="88" height="86" viewBox="0 0 88 86" aria-label="Music note">
        <g fill="none" stroke="#2c2c2c" stroke-width="6">
          <ellipse cx="17" cy="71" rx="13" ry="10"/>
          <ellipse cx="70" cy="61" rx="13" ry="10"/>
          <path d="M30 70V16L83 5v56M30 30L83 19"/>
        </g>
      </svg>
      <h3>AFRO POP</h3>
      <p>Sed ut perspiciatis unde omnis iste natus error sit voluptatem accusan-tium doloremque laudantium, totam dicta sunt explicabo.</p>
    </div>
    <div class="genre">
      <div class="genre-art" style="left:20px" role="img" aria-label="Silhouette of a dancer in a flowing dress"></div>
      <h3 style="left:136px">DANCEHALL</h3>
      <p style="left:136px">Sed ut perspiciatis unde omnis iste natus error sit voluptatem accusan-tium doloremque laudantium, totam dicta sunt explicabo.</p>
    </div>
  </section>

  <div class="social">
    <span aria-label="Social link"></span>
    <span aria-label="Social link"></span>
    <span aria-label="Social link"></span>
    <span aria-label="Social link"></span>
    <span aria-label="Social link"></span>
    <span aria-label="Email"><svg width="17" height="13" viewBox="0 0 17 13"><rect x="1" y="1" width="15" height="11" rx="1.5" fill="none" stroke="#999" stroke-width="1.5"/><path d="M1.5 2l7 5.5 7-5.5" fill="none" stroke="#999" stroke-width="1.5"/></svg></span>
  </div>

  <nav class="footer-nav">
    <span>HOME</span><span>|</span><span>MUSIC</span><span>|</span><span>ARTISTE</span><span>|</span><span>NEWS</span><span>|</span><span>LOGIN</span>
  </nav>
  <p class="copy">© Copyrights 2017 Vorlen Music.All Rights Reserved.</p>
</div>
</body>
</html>
```